Australian Software Consultancy needs new Business Card Design

Design Business Card based on existing design artefacts (attached). We are open to all designs. As its a 2 sided design and we thought it might be quite striking to have one side with a black background and te other side with a white background.

Target Market(s)

Financial Services mainly.

Industry/Entity Type

Business

Contact Information for Business Card

Name :
Position :
Email :

Requirements
Must have
• Funky design using our existing assets

```html
<!DOCTYPE html>
<html lang="en">
<head>
<meta charset="utf-8">
<title>Northbeam Business Card</title>
<link rel="stylesheet" href="https://fonts.googleapis.com/css2?family=Quicksand:wght@400;500;700&display=swap">
<style>
  :root {
    --backdrop-top: #5f676d;
    --backdrop-bottom: #3e4449;
    --card-black: #050505;
    --card-white: #ffffff;
    --accent-red: #e8242a;
    --ink: #111111;
    --ink-soft: #333333;
  }
  * { margin: 0; padding: 0; box-sizing: border-box; }
  html, body {
    width: 1200px;
    height: 900px;
    overflow: hidden;
  }
  body {
    background: radial-gradient(ellipse at 50% 35%, var(--backdrop-top), var(--backdrop-bottom));
    font-family: "Quicksand", sans-serif;
    position: relative;
  }
  .card {
    position: absolute;
    left: 250px;
    width: 700px;
    height: 400px;
    overflow: hidden;
    box-shadow: 0 10px 26px rgba(0,0,0,0.45);
  }
  .card--front { top: 40px; background: var(--card-black); }
  .card--back { top: 470px; background: var(--card-black); }

  .front-panel {
    position: absolute;
    inset: 0;
  }
  .wordmark {
    position: absolute;
    left: 235px;
    top: 42px;
    font-size: 40px;
    font-weight: 700;
    letter-spacing: 1px;
    color: var(--ink);
  }
  .contact-list {
    position: absolute;
    left: 130px;
    top: 140px;
    list-style: none;
  }
  .contact-item {
    display: flex;
    align-items: flex-start;
    gap: 16px;
    margin-bottom: 30px;
  }
  .contact-icon {
    width: 44px;
    height: 30px;
    flex: none;
  }
  .contact-text {
    font-size: 15px;
    font-weight: 500;
    line-height: 1.25;
    color: var(--ink);
    padding-top: 2px;
  }
  .person {
    position: absolute;
    right: 60px;
    top: 175px;
    text-align: right;
  }
  .person-name {
    font-size: 30px;
    font-weight: 500;
    letter-spacing: 0.5px;
    color: var(--ink);
  }
  .person-name .first { color: var(--accent-red); font-weight: 700; }
  .person-role {
    font-size: 15px;
    color: var(--ink-soft);
  }

  .back-brand {
    position: absolute;
    inset: 0;
    display: flex;
    align-items: center;
    justify-content: center;
  }
  .brand-name {
    font-size: 60px;
    font-weight: 700;
    letter-spacing: 2px;
    color: var(--accent-red);
  }
</style>
</head>
<body>

<section class="card card--front" aria-label="Business card front">
  <svg class="front-panel" width="700" height="400" viewBox="0 0 700 400" aria-hidden="true">
    <polygon points="215,0 700,0 700,400 120,400 170,60" fill="var(--card-white)"/>
  </svg>

  <div class="wordmark">NORTHBEAM</div>

  <ul class="contact-list">
    <li class="contact-item">
      <svg class="contact-icon" viewBox="0 0 44 30" aria-hidden="true">
        <polygon points="0,15 14,0 44,0 44,30 14,30" fill="var(--accent-red)"/>
        <path d="M22 8 c-2 2 -2 6 2 10 s8 4 10 2 l-3 -3 -2 2 c-2 -1 -4 -3 -5 -5 l2 -2 z" fill="#fff"/>
      </svg>
      <span class="contact-text">+0000 1234 5678<br>+0000 1234 5678</span>
    </li>
    <li class="contact-item">
      <svg class="contact-icon" viewBox="0 0 44 30" aria-hidden="true">
        <polygon points="0,15 14,0 44,0 44,30 14,30" fill="var(--accent-red)"/>
        <circle cx="28" cy="15" r="8" fill="none" stroke="#fff" stroke-width="1.5"/>
        <line x1="20" y1="15" x2="36" y2="15" stroke="#fff" stroke-width="1.2"/>
        <ellipse cx="28" cy="15" rx="3.5" ry="8" fill="none" stroke="#fff" stroke-width="1.2"/>
      </svg>
      <span class="contact-text">yourname@mail.com<br>www.yourwebsite.com</span>
    </li>
    <li class="contact-item">
      <svg class="contact-icon" viewBox="0 0 44 30" aria-hidden="true">
        <polygon points="0,15 14,0 44,0 44,30 14,30" fill="var(--accent-red)"/>
        <path d="M28 24 c-5 -6 -7 -9 -7 -12 a7 7 0 0 1 14 0 c0 3 -2 6 -7 12 z" fill="#fff"/>
        <circle cx="28" cy="12" r="2.6" fill="var(--accent-red)"/>
      </svg>
      <span class="contact-text">Street address here<br>Bangladesh,1215</span>
    </li>
  </ul>

  <div class="person">
    <div class="person-name"><span class="first">JHON</span> DOE</div>
    <div class="person-role">Owner</div>
  </div>
</section>

<section class="card card--back" aria-label="Business card back">
  <div class="back-brand">
    <div class="brand-name">NORTHBEAM</div>
  </div>
</section>

</body>
</html>
```